Business Card Design Project

We need business cards for our new business, Vantrel Optics. We specialize in aerial videography and photography via drone. Currently we are mainly focusing on real estate videography but will branch into other markets and may even host training classes for flying drones.
Updates
Cards should include:
Name
Phone Number
Email Address
Web address
We will need to customize for more than one person and would like those fields to be editable
eps file logos are uploaded now, thanks!
Target Market(s)
Real Estate Agents, hotels, rental agencies and people who have recently purchase drones
Industry/Entity Type
Videography
Font styles to use
Look and feel
Each slider illustrates characteristics of the customer's brand and the style your logo design should communicate.

```html
<!DOCTYPE html>
<html lang="en">
<head>
<meta charset="utf-8">
<title>Vantrel Optics — Business Card</title>
<link href="https://fonts.googleapis.com/css2?family=Roboto:wght@400;500&family=Rajdhani:wght@500&display=swap" rel="stylesheet">
<style>
  :root {
    --stage: #e9e6e1;
    --card-front: #ffffff;
    --card-back: #0b0b0b;
    --ink-dark: #2b2b2b;
    --accent: #f4a81b;
    --gold: #f2c12e;
    --text-light: #f2f2f2;
  }
  html, body {
    margin: 0;
    padding: 0;
    width: 1200px;
    height: 533px;
    overflow: hidden;
    background: var(--stage);
  }
  .card {
    position: absolute;
    left: 120px;
    top: 127px;
    width: 960px;
    height: 279px;
    display: flex;
    box-shadow: 0 3px 8px rgba(0,0,0,0.18);
  }
  .card-front {
    width: 480px;
    height: 100%;
    background: var(--card-front);
    position: relative;
  }
  .brand {
    position: absolute;
    left: 100px;
    top: 108px;
    display: flex;
    align-items: center;
    gap: 12px;
  }
  .brand-mark {
    width: 48px;
    height: 48px;
    background: var(--accent);
  }
  .brand-name {
    font-family: "Roboto", sans-serif;
    font-weight: 500;
    font-size: 34px;
    letter-spacing: 1px;
    color: var(--ink-dark);
    line-height: 1;
    white-space: nowrap;
  }
  .card-back {
    width: 480px;
    height: 100%;
    background: var(--card-back);
    position: relative;
  }
  .contact {
    position: absolute;
    left: 248px;
    top: 129px;
    font-family: "Roboto", sans-serif;
    color: var(--text-light);
  }
  .person-name {
    font-family: "Rajdhani", sans-serif;
    font-weight: 500;
    font-size: 18px;
    letter-spacing: 0.5px;
    color: var(--gold);
    margin: 0 0 18px 0;
    line-height: 1;
  }
  .address {
    font-size: 11px;
    line-height: 13.5px;
    margin: 0 0 8px 0;
    font-style: normal;
  }
  .links {
    list-style: none;
    margin: 0;
    padding: 0;
    font-size: 11px;
    line-height: 13.5px;
  }
  .links li {
    display: flex;
    align-items: center;
    gap: 3px;
  }
  .links svg {
    width: 7px;
    height: 7px;
    flex: none;
  }
</style>
</head>
<body>
  <div class="card">
    <section class="card-front">
      <div class="brand">
        <span class="brand-mark"></span>
        <span class="brand-name">VANTREL OPTICS</span>
      </div>
    </section>
    <section class="card-back">
      <div class="contact">
        <p class="person-name">ARUN KESAR</p>
        <address class="address">
          214, Maple Crest Homes,<br>
          2nd Cross, 6th main,<br>
          LV Colony, HSR Layout,<br>
          Sunnapura, Bangalore-560 048
        </address>
        <ul class="links">
          <li>
            <svg viewBox="0 0 8 8"><rect x="1.5" y="0" width="5" height="8" rx="1" fill="#f2f2f2"/><rect x="2.5" y="1" width="3" height="5" fill="#0b0b0b"/></svg>
            98400 217 63
          </li>
          <li>
            <svg viewBox="0 0 8 8"><rect x="0.5" y="1.5" width="7" height="5" fill="none" stroke="#f2f2f2" stroke-width="1"/><path d="M0.5 1.5 L4 4.5 L7.5 1.5" fill="none" stroke="#f2f2f2" stroke-width="0.8"/></svg>
            info@vantrel.com
          </li>
          <li>
            <svg viewBox="0 0 8 8"><rect x="0.5" y="0.5" width="7" height="7" fill="none" stroke="#f2f2f2" stroke-width="1"/><rect x="2.5" y="2.5" width="3" height="3" fill="#f2f2f2"/></svg>
            vantrel.com
          </li>
        </ul>
      </div>
    </section>
  </div>
</body>
</html>
```